Responsive Website Design for New Social Site (Building User Account)

KelvaPost.com is a website that allows people to create preformatted emails to be sent out at a later date. The purpose is to allow people to communicate in the event of an accident or death. The beta site is built but not consumable by the public. It needs a new look before we go live.

I’m speaking specifically about the user account. They are admin tools for creating and publishing communications. They include workflow design, document/message storage, and a dashboard.

I currently have a basic design. Now I’m looking for an inspired design. Something interesting and memorable. Something that draws people in. I have a PPT that can provide guidance on what elements need to be on each page but I’m looking for someone who knows how to create engaging websites.

SCOPE OF EFFORT
There are approximately 23 pages to the website but only 5 distinct page appearances
• Dashboard
• Workflow
• Document/Message/Contact Management
• Education Search
• Account Form
I need a few pop-up designs
• Yes/No/Continue
I need a responsive design (3 sizes)

ARTISTIC QUALITIES
Easy to Use/Understand
New/Inventive/Cool/Memorable
Works with the Logo
Consistent Elements (buttons, text, use of color, etc)

TECHNICAL ASPECTS
I’d like the work provided in a storyboard and individual files for development

PHASES
1. Initial Concept
a. 2-3 Designs Ideas. Just the Dashboard and Workflow in responsive formats
2. Build
a. Create all the pages
b. Provide in storyboard in responsive formats
c. 2 Rounds of Revision
3. Final
a. Provide Storyboard and Files

I'd like to see a portfolio of your responsive web design, especially any user accounts you have created. I've attached three of the initial pages. I'd like to see a concept of what you would produce for at least one of the pages.

Thank you for your interest.

```html
<!DOCTYPE html>
<html lang="en">
<head>
<meta charset="utf-8">
<title>KelvaPost – Dashboard</title>
<link href="https://fonts.googleapis.com/css2?family=Lato:wght@400;700&display=swap" rel="stylesheet">
<style>
:root{
  --orange:#f47920;
  --ink:#2b2b2b;
  --text:#333;
  --muted:#777;
  --icon:#8a8a8a;
  --nav:#2f2f2f;
  --nav-active:#1f1f1f;
  --nav-text:#c9c9c9;
  --band:#e4e4e4;
  --page:#f6f6f6;
  --card:#fdfdfd;
  --line:#dcdcdc;
  --row-alt:#f1f1f1;
  --brand:#1e88c8;
}
*{box-sizing:border-box;margin:0;padding:0}
html,body{width:1200px;height:1103px;overflow:hidden}
body{font-family:"Lato",sans-serif;background:var(--page);color:var(--text);position:relative}
.abs{position:absolute}

.site-header{position:absolute;left:0;top:0;width:1200px;height:78px;background:#fff}
.brand{position:absolute;left:86px;top:12px;display:flex;align-items:center;gap:10px}
.brand-dot{width:40px;height:40px;border-radius:50%;background:var(--brand)}
.brand-name{font-size:34px;font-weight:700;color:var(--brand);line-height:1}
.brand-tag{position:absolute;left:136px;top:50px;font-size:10px;color:#444;white-space:nowrap}
.auth-btn{position:absolute;top:22px;height:36px;width:135px;border:1px solid #bbb;border-radius:4px;
  background:linear-gradient(#fff,#e9e9e9);box-shadow:0 2px 3px rgba(0,0,0,.25);display:flex;align-items:center;
  font-weight:700;font-size:14px;color:#111;overflow:hidden}
.auth-btn span{flex:1;text-align:center}
.auth-btn i{width:30px;height:100%;background:linear-gradient(#bdbdbd,#9a9a9a);display:flex;align-items:center;justify-content:center}
.auth-login{left:816px}
.auth-signup{left:978px}

.main-nav{position:absolute;left:0;top:78px;width:1200px;height:123px;
  background:repeating-linear-gradient(45deg,#333 0 2px,#2c2c2c 2px 4px)}
.user-box{position:absolute;left:86px;top:20px;width:73px;height:83px;background:#e8e8e8;border-radius:3px;text-align:center;padding-top:6px}
.user-box .name{font-size:13px;color:#222;margin-top:2px}
.user-box .logout{font-size:12px;color:var(--orange)}
.nav-item{position:absolute;top:20px;width:88px;height:86px;text-align:center;color:var(--nav-text);font-size:14px;padding-top:18px;margin-left:-44px}
.nav-item svg{display:block;margin:0 auto 6px}
.nav-item.active{background:var(--nav-active);color:#fff;border-radius:3px}
.nav-pointer{position:absolute;left:391px;top:114px;width:0;height:0;border-left:7px solid transparent;border-right:7px solid transparent;border-bottom:9px solid var(--band)}

.promo-band{position:absolute;left:0;top:201px;width:1200px;height:36px;background:var(--band);border-bottom:1px solid #d4d4d4;
  text-align:center;line-height:36px;font-size:14px;color:#222}

.dashboard{position:absolute;left:86px;top:270px;width:1027px;height:767px;background:var(--card);border:1px solid var(--line);border-radius:4px}
.stat{position:absolute;top:36px}
.stat-count{position:absolute;left:0;top:0;width:55px;height:55px;border-radius:50%;background:var(--orange);color:#222;
  font-size:26px;display:flex;align-items:center;justify-content:center}
.stat-title{position:absolute;left:68px;top:-2px;font-size:22px;color:var(--orange);white-space:nowrap}
.stat-text{position:absolute;left:68px;top:22px;width:190px;font-size:13px;line-height:21px;color:var(--muted)}

.section-title{position:absolute;left:16px;font-size:22px;color:var(--ink)}
.section-title::after{content:"";position:absolute;left:0;bottom:-9px;height:3px;background:var(--ink)}
.title-recommended{top:150px}
.title-recommended::after{width:122px}
.title-active{top:324px}
.title-active::after{width:41px}

.plan-bar{position:absolute;left:16px;top:217px;width:996px;height:77px;background:#efefef;border:1px solid #d6d6d6;border-radius:4px}
.plan-type{position:absolute;top:0;height:77px;display:flex;align-items:center;gap:8px;font-size:22px;color:var(--muted)}
.plan-divider{position:absolute;top:14px;width:1px;height:50px;background:#cfcfcf}

.plans-table{position:absolute;left:16px;top:392px;width:996px;border-collapse:collapse;font-size:14px}
.plans-table th{background:var(--orange);color:#222;font-weight:400;height:38px;border-bottom:2px solid #e06a14}
.plans-table td{height:38.9px;color:#222}
.plans-table tbody tr:nth-child(even){background:var(--row-alt)}
.plans-table th,.plans-table td{text-align:center}
.plans-table .col-status{text-align:left;padding-left:22px}
.plans-table .col-contact{padding-left:58px}

.site-footer{position:absolute;left:0;top:1061px;width:1200px;text-align:center;font-size:13.5px;color:#222}
</style>
</head>
<body>

<header class="site-header">
  <div class="brand"><span class="brand-dot"></span><span class="brand-name">KelvaPost</span></div>
  <div class="brand-tag">The most trusted resource for life management</div>
  <a class="auth-btn auth-login"><span>LOGIN</span><i><svg width="16" height="18" viewBox="0 0 16 18"><circle cx="8" cy="5" r="4" fill="#fff"/><path d="M0 18c0-6 3-8 8-8s8 2 8 8z" fill="#fff"/></svg></i></a>
  <a class="auth-btn auth-signup"><span>SIGNUP</span><i><svg width="16" height="16" viewBox="0 0 16 16"><path d="M2 14l1-4 8-8 3 3-8 8z" fill="#fff"/></svg></i></a>
</header>

<nav class="main-nav">
  <div class="user-box">
    <svg width="32" height="32" viewBox="0 0 32 32"><circle cx="16" cy="10" r="7" fill="#222"/><path d="M2 32c0-10 6-13 14-13s14 3 14 13z" fill="#222"/></svg>
    <div class="name">Dana Reed</div>
    <div class="logout">Logout</div>
  </div>

  <div class="nav-item active" style="left:398px">
    <svg width="26" height="24" viewBox="0 0 26 24"><path d="M13 1L1 12h4v11h6v-7h4v7h6V12h4z" fill="var(--orange)"/></svg>Home</div>
  <div class="nav-item" style="left:512px">
    <svg width="28" height="26" viewBox="0 0 28 26" fill="none" stroke="var(--nav-text)" stroke-width="2"><circle cx="14" cy="6" r="5"/><circle cx="6" cy="13" r="5"/><circle cx="22" cy="13" r="5"/><circle cx="14" cy="20" r="5"/></svg>Plans</div>
  <div class="nav-item" style="left:618px">
    <svg width="22" height="26" viewBox="0 0 22 26" fill="none" stroke="var(--nav-text)" stroke-width="2"><path d="M2 1h13l5 5v19H2z"/><path d="M6 10h10M6 15h10M6 20h10"/></svg>Documents</div>
  <div class="nav-item" style="left:738px">
    <svg width="30" height="22" viewBox="0 0 30 22"><rect x="1" y="1" width="28" height="20" fill="var(--nav-text)"/><path d="M1 1l14 11L29 1" fill="none" stroke="#333" stroke-width="2"/></svg>Messages</div>
  <div class="nav-item" style="left:851px">
    <svg width="30" height="24" viewBox="0 0 30 24"><rect x="1" y="4" width="28" height="19" rx="2" fill="var(--nav-text)"/><rect x="10" y="1" width="10" height="5" fill="var(--nav-text)"/><circle cx="9" cy="12" r="3" fill="#333"/><path d="M4 20c0-4 2-5 5-5s5 1 5 5z" fill="#333"/><path d="M17 11h9M17 15h9" stroke="#333" stroke-width="2"/></svg>Contacts</div>
  <div class="nav-item" style="left:960px">
    <svg width="30" height="26" viewBox="0 0 30 26" fill="none" stroke="var(--nav-text)" stroke-width="2"><path d="M15 2v22M8 24h14M4 6h22"/><path d="M4 6l-3 9h6zM26 6l-3 9h6z"/></svg>Learning</div>
  <div class="nav-item" style="left:1077px">
    <svg width="30" height="26" viewBox="0 0 30 26" fill="var(--nav-text)"><circle cx="8" cy="5" r="4"/><circle cx="22" cy="5" r="4"/><circle cx="15" cy="11" r="4"/><path d="M1 20c0-6 3-8 7-8s7 2 7 8zM15 20c0-6 3-8 7-8s7 2 7 8zM8 26c0-6 3-8 7-8s7 2 7 8z"/></svg>Community</div>

  <div class="nav-pointer"></div>
</nav>

<div class="promo-band">Discover Why KelvaPost is Important to You</div>

<main class="dashboard">
  <div class="stat" style="left:16px"><div class="stat-count">4</div><div class="stat-title">Plans</div><div class="stat-text">Lorem Ipsum is simply dummy text of the printing and typesetting industry. Lorem</div></div>
  <div class="stat" style="left:272px"><div class="stat-count">12</div><div class="stat-title">Contacts</div><div class="stat-text">Lorem Ipsum is simply dummy text of the printing and typesetting industry. Lorem</div></div>
  <div class="stat" style="left:526px"><div class="stat-count">4</div><div class="stat-title">Documents</div><div class="stat-text">Lorem Ipsum is simply dummy text of the printing and typesetting industry. Lorem</div></div>
  <div class="stat" style="left:776px"><div class="stat-count">10</div><div class="stat-title">Messages</div><div class="stat-text">Lorem Ipsum is simply dummy text of the printing and typesetting industry. Lorem</div></div>

  <h2 class="section-title title-recommended" style="font-weight:400">Recommended Plans</h2>

  <div class="plan-bar">
    <div class="plan-type" style="left:58px">
      <svg width="34" height="34" viewBox="0 0 34 34"><circle cx="17" cy="17" r="13" fill="none" stroke="var(--icon)" stroke-width="7"/><circle cx="17" cy="17" r="13" fill="none" stroke="#efefef" stroke-width="7" stroke-dasharray="7 13.4"/></svg>Life</div>
    <div class="plan-divider" style="left:158px"></div>
    <div class="plan-type" style="left:184px">
      <svg width="28" height="34" viewBox="0 0 28 34" fill="var(--icon)"><circle cx="14" cy="7" r="6"/><path d="M2 34V20c0-5 4-8 12-8s12 3 12 8v14z"/></svg>Accident</div>
    <div class="plan-divider" style="left:336px"></div>
    <div class="plan-type" style="left:366px">
      <svg width="36" height="32" viewBox="0 0 36 32" fill="var(--icon)"><path d="M18 1L1 16h5v15h9v-9h6v9h9V16h5z"/></svg>Home</div>
    <div class="plan-divider" style="left:492px"></div>
    <div class="plan-type" style="left:522px">
      <svg width="34" height="30" viewBox="0 0 34 30" fill="var(--icon)"><path d="M7 4h20l4 10h2v10h-3v5h-5v-5H9v5H4v-5H1V14h2z"/><rect x="10" y="7" width="14" height="6" fill="#efefef"/><circle cx="7" cy="19" r="2.5" fill="#efefef"/><circle cx="27" cy="19" r="2.5" fill="#efefef"/></svg>Auto</div>
    <div class="plan-divider" style="left:641px"></div>
    <div class="plan-type" style="left:672px">
      <svg width="32" height="32" viewBox="0 0 32 32" fill="none" stroke="var(--icon)" stroke-width="2.5"><circle cx="16" cy="16" r="13"/><ellipse cx="16" cy="16" rx="6" ry="13"/><path d="M3 16h26M6 9h20M6 23h20"/></svg>Travel</div>
    <div class="plan-divider" style="left:792px"></div>
    <div class="plan-type" style="left:821px">
      <svg width="54" height="16" viewBox="0 0 54 16" fill="none" stroke="var(--icon)" stroke-width="3"><circle cx="8" cy="8" r="6"/><circle cx="27" cy="8" r="6"/><circle cx="46" cy="8" r="6"/></svg>More</div>
  </div>

  <h2 class="section-title title-active" style="font-weight:400">Active Plans</h2>

  <table class="plans-table">
    <colgroup><col style="width:120px"><col style="width:198px"><col style="width:160px"><col style="width:216px"><col style="width:136px"><col style="width:166px"></colgroup>
    <thead><tr><th class="col-status">Status</th><th>Plan Name</th><th>Start Date</th><th>End Date</th><th>Documents</th><th class="col-contact">Contact</th></tr></thead>
    <tbody>
      <tr><td class="col-status">Start</td><td>Lorem Ipsum dollar</td><td>10/8/2015</td><td>15/10/2015</td><td>3</td><td class="col-contact">8</td></tr>
      <tr><td class="col-status">Start</td><td>Lorem Ipsum dollar</td><td>10/8/2015</td><td>15/10/2015</td><td>3</td><td class="col-contact">8</td></tr>
      <tr><td class="col-status">Start</td><td>Lorem Ipsum dollar</td><td>10/8/2015</td><td>15/10/2015</td><td>3</td><td class="col-contact">8</td></tr>
      <tr><td class="col-status">Start</td><td>Lorem Ipsum dollar</td><td>10/8/2015</td><td>15/10/2015</td><td>3</td><td class="col-contact">8</td></tr>
      <tr><td class="col-status">Start</td><td>Lorem Ipsum dollar</td><td>10/8/2015</td><td>15/10/2015</td><td>3</td><td class="col-contact">8</td></tr>
      <tr><td class="col-status">Start</td><td>Lorem Ipsum dollar</td><td>10/8/2015</td><td>15/10/2015</td><td>3</td><td class="col-contact">8</td></tr>
      <tr><td class="col-status">Start</td><td>Lorem Ipsum dollar</td><td>10/8/2015</td><td>15/10/2015</td><td>3</td><td class="col-contact">8</td></tr>
      <tr><td class="col-status">Start</td><td>Lorem Ipsum dollar</td><td>10/8/2015</td><td>15/10/2015</td><td>3</td><td class="col-contact">8</td></tr>
    </tbody>
  </table>
</main>

<footer class="site-footer">Copyright © 2015 KelvaPost. All Rights Reserved.</footer>

</body>
</html>
```